Security based company delivering Hazard Line Training to Law Enforcement Agencies Worldwide.

We need a Web design for a company doing business in Washington D.C. We deliver Hazard Line Training to Law Enforcement Agencies throughout the world. Our focus is on Improvised Explosive Devices. We train Bomb Technicians and First Responders in all aspects relating to bombings and criminal incidents globally.

Reason: We have uploaded our logo. Thank you.

Target Market(s)

Military and Law Enforcement Personnel from around the world.

Industry/Entity Type

Business

Requirements
Should not have
• Do not include cartoon like characters.

```html
<!DOCTYPE html>
<html lang="en">
<head>
<meta charset="utf-8">
<title>Ridgeway Tactical</title>
<link href="https://fonts.googleapis.com/css2?family=Lato:wght@400;700&family=Open+Sans:wght@400;600;700&family=Oswald:wght@400&display=swap" rel="stylesheet">
<style>
:root{
  --ink:#1e1e1e;
  --dark:#252525;
  --navy:#1f3140;
  --navy-top:#2a4257;
  --orange:#e0902a;
  --light:#f1f1f1;
  --white:#ffffff;
  --body:#4a4a4a;
}
*{box-sizing:border-box;margin:0;padding:0}
html,body{width:798px;height:1200px;overflow:hidden;background:var(--white);font-family:"Lato",sans-serif;color:var(--ink)}
.page{position:relative;width:798px;height:1200px;overflow:hidden}
.abs{position:absolute}

/* header */
.header{top:0;left:0;width:798px;height:56px;border-top:3px solid var(--ink);background:var(--white)}
.brand{left:80px;top:14px;font-family:"Oswald",sans-serif;font-size:21px;letter-spacing:.2px;color:var(--ink)}
.utility{left:513px;top:0;width:208px;height:19px;background:var(--ink);color:var(--white);font-size:10px;display:flex;align-items:center;gap:7px;padding-left:12px;white-space:nowrap}
.utility svg{flex:none}
.search{left:512px;top:28px;width:123px;height:21px;background:#ececec;font-size:10px;color:#a8a8a8;padding:5px 6px}
.search-btn{left:611px;top:28px;width:24px;height:21px;background:var(--ink);display:flex;align-items:center;justify-content:center}
.socials{left:645px;top:31px;display:flex;gap:4px}
.socials span{width:15px;height:15px;background:var(--ink);border-radius:2px}

/* nav */
.nav{top:56px;left:0;width:798px;height:35px;background:linear-gradient(var(--navy-top),var(--navy));display:flex;align-items:center;padding-left:86px}
.nav a{color:var(--white);font-size:12px;text-decoration:none;margin-right:20px;white-space:nowrap}

/* hero */
.hero{top:91px;left:0;width:798px;height:242px;background:linear-gradient(180deg,#8aa0b8 0%,#b9b3a6 30%,#b89b78 55%,#a9875f 100%);border-bottom:2px solid var(--orange)}
.hero-title{left:68px;top:54px;width:271px;height:104px;background:rgba(240,240,240,.85);border-left:5px solid #333;padding:2px 0 0 6px;font-family:"Open Sans",sans-serif;font-weight:700;font-size:17px;line-height:33px;letter-spacing:-.1px;color:var(--ink);white-space:nowrap;overflow:hidden}
.hero-btn{left:69px;top:172px;width:80px;height:21px;background:var(--ink);color:var(--white);font-family:"Open Sans",sans-serif;font-weight:700;font-size:8.5px;display:flex;align-items:center;justify-content:center}
.hero-arrow{top:96px}
.dots{left:361px;top:223px;width:77px;height:17px;background:var(--ink);display:flex;align-items:center;justify-content:center;gap:6px}
.dots i{width:6px;height:6px;border-radius:50%;background:#888}
.dots i.on{background:#ddd}

/* welcome */
.welcome{top:333px;left:0;width:798px;height:191px;background:var(--dark);color:var(--white)}
.welcome h2{position:absolute;top:28px;font-family:"Open Sans",sans-serif;font-weight:400;font-size:17px;white-space:nowrap}
.welcome p{position:absolute;left:72px;top:66px;width:390px;font-size:8.4px;line-height:16px}
.divider{left:482px;top:16px;width:1px;height:158px;background:#151515;box-shadow:2px 0 4px rgba(0,0,0,.4)}
.why-list{left:524px;top:62px;width:173px;list-style:none}
.why-list li{height:30.5px;display:flex;align-items:center;gap:5px;font-family:"Open Sans",sans-serif;font-size:9.5px;border-bottom:1px dashed #8a8a8a;white-space:nowrap}
.why-list li:last-child{border-bottom:none}

/* cards */
.card{top:536px;width:205px;height:236px;background:#fbf7f7;border:1px solid #d8d8d8;border-top:5px solid var(--ink);text-align:center}
.card::after{content:"";position:absolute;left:30px;right:30px;bottom:-12px;height:10px;border-radius:50%;background:radial-gradient(rgba(0,0,0,.45),rgba(0,0,0,0) 70%)}
.card h3{font-family:"Open Sans",sans-serif;font-weight:400;font-size:16px;margin-top:13px;white-space:nowrap}
.card .thumb{width:155px;height:60px;margin:6px auto 0}
.card p{width:166px;margin:12px auto 0;font-size:8.3px;line-height:16px;color:var(--body);text-align:justify;text-align-last:center}
.card .btn{width:82px;height:24px;margin:9px auto 0;background:var(--ink);color:var(--white);font-family:"Open Sans",sans-serif;font-weight:700;font-size:8.5px;display:flex;align-items:center;justify-content:center}

/* gallery */
.gallery-title{left:70px;top:797px;font-family:"Open Sans",sans-serif;font-weight:400;font-size:16px}
.tile{top:826px;width:150px;height:135px}
.tile .img{height:113px}
.tile .cap{height:22px;background:var(--ink);color:var(--white);font-size:8.5px;display:flex;align-items:center;justify-content:space-between;padding:0 8px 0 20px;white-space:nowrap}

/* news band */
.news{top:976px;left:0;width:798px;height:53px;background:var(--light)}
.news h3{position:absolute;left:77px;top:17px;font-family:"Open Sans",sans-serif;font-weight:600;font-size:13px;color:#2a2a2a}
.news .bar{position:absolute;left:201px;top:11px;width:1.5px;height:33px;background:#333}
.news p{position:absolute;left:216px;top:20px;font-size:8.5px;color:#333;white-space:nowrap}

/* footer */
.footer{top:1029px;left:0;width:798px;height:171px;background:var(--dark);color:var(--white)}
.col{position:absolute;top:15px}
.col h4{font-family:"Open Sans",sans-serif;font-weight:600;font-size:11.5px;margin-bottom:10px;white-space:nowrap}
.col h5{font-family:"Open Sans",sans-serif;font-weight:600;font-size:8.5px;margin:-2px 0 6px;white-space:nowrap}
.about p{width:138px;font-size:8px;line-height:16px;text-align:justify;hyphens:auto;-webkit-hyphens:auto}
.links ul{list-style:none}
.links li{font-size:8.5px;line-height:16px}
.reach p{font-size:7.8px;line-height:14px;white-space:nowrap}
.letter p{font-size:8.5px}
.field{width:146px;height:25px;background:var(--white);margin-top:8px;font-size:7.5px;color:#aaa;padding:8px 11px}
.send{width:46px;height:21px;border:1px solid #ddd;margin-top:9px;font-size:8px;display:flex;align-items:center;justify-content:center}
.mini{display:flex;gap:11px;margin-top:12px}
.mini span{width:8px;height:8px;background:#eee;border-radius:50%}
</style>
</head>
<body>
<div class="page">

  <header class="header abs">
    <div class="brand abs">RIDGEWAY TACTICAL</div>
    <div class="utility abs">
      <svg width="8" height="8" viewBox="0 0 10 10"><path d="M2 0l2 2.5-1 1.2c.7 1.4 1.7 2.4 3.1 3.1l1.2-1L10 8l-1.3 2C4.7 9.6.4 5.3 0 1.3z" fill="#fff"/></svg>
      <span>+10005550142</span>
      <svg width="8" height="8" viewBox="0 0 10 10" style="margin-left:8px"><circle cx="5" cy="3" r="2.6" fill="#fff"/><path d="M0 10c0-3 2-4.5 5-4.5S10 7 10 10z" fill="#fff"/></svg>
      <span>Register</span>
      <svg width="7" height="8" viewBox="0 0 8 10"><path d="M2 4V3a2 2 0 014 0v1" stroke="#fff" fill="none" stroke-width="1.3"/><rect y="4" width="8" height="6" fill="#fff"/></svg>
      <span>Login</span>
    </div>
    <div class="search abs">Search....</div>
    <div class="search-btn abs"><svg width="11" height="11" viewBox="0 0 12 12"><circle cx="5" cy="5" r="3.6" stroke="#fff" stroke-width="1.6" fill="none"/><path d="M7.7 7.7L11 11" stroke="#fff" stroke-width="1.8"/></svg></div>
    <div class="socials abs"><span></span><span></span><span></span><span></span></div>
  </header>

  <nav class="nav abs">
    <a>Home</a><a>About Us</a><a>IED Training</a><a>Equipments</a><a>Solutions</a><a>Our Trainers</a><a>Resources</a><a>News</a><a>Contact Us</a>
  </nav>

  <section class="hero abs" role="img" aria-label="Photo of a controlled explosive blast in a desert training field">
    <svg class="hero-arrow abs" style="left:16px" width="12" height="20" viewBox="0 0 12 20"><path d="M10 2L3 10l7 8" stroke="#fff" stroke-width="2.5" fill="none"/></svg>
    <svg class="hero-arrow abs" style="left:779px" width="12" height="20" viewBox="0 0 12 20"><path d="M2 2l7 8-7 8" stroke="#fff" stroke-width="2.5" fill="none"/></svg>
    <div class="hero-title abs">PUTTING IN PLACE LASTING<br>SOLUTIONS THAT<br>MAKE AN IMPACT</div>
    <div class="hero-btn abs">Read More.....</div>
    <div class="dots abs"><i></i><i class="on"></i><i></i></div>
  </section>

  <section class="welcome abs">
    <h2 style="left:73px">Welcome To Hazard Line Training</h2>
    <p>We need a Web design for a company doing business in Washington D.C. We deliver Hazard Line Training to Law Enforcement Agencies throughout the world. Our focus is on Improvised Explosive Devices. We train Bomb Technicians and First Responders in all aspects relating to bombings and criminal incidents globally.</p>
    <div class="divider abs"></div>
    <h2 style="left:518px">Why Hazard Line Training ?</h2>
    <ul class="why-list abs">
      <li><svg width="7" height="7" viewBox="0 0 8 8"><path d="M1 1l3 3-3 3M4 1l3 3-3 3" stroke="#fff" fill="none"/></svg>High Value</li>
      <li><svg width="7" height="7" viewBox="0 0 8 8"><path d="M1 1l3 3-3 3M4 1l3 3-3 3" stroke="#fff" fill="none"/></svg>Commited to your Satisfaction</li>
      <li><svg width="7" height="7" viewBox="0 0 8 8"><path d="M1 1l3 3-3 3M4 1l3 3-3 3" stroke="#fff" fill="none"/></svg>Geotechnical Expertise</li>
      <li><svg width="7" height="7" viewBox="0 0 8 8"><path d="M1 1l3 3-3 3M4 1l3 3-3 3" stroke="#fff" fill="none"/></svg>Dedicated well trained crews</li>
    </ul>
  </section>

  <article class="card abs" style="left:68px">
    <h3>Explosive Mangment</h3>
    <div class="thumb" role="img" aria-label="Photo of soldiers silhouetted against an orange sunset" style="background:linear-gradient(180deg,#e9a21a,#b9700c)"></div>
    <p>We need a Web design for a company doing business in Washington D.C. We deliver Hazard Line Training to Law Enforcement Agencies throughout the world. Our focus is</p>
    <div class="btn">Read More...</div>
  </article>
  <article class="card abs" style="left:298px">
    <h3>Learning</h3>
    <div class="thumb" role="img" aria-label="Photo of reading glasses resting on an open book" style="background:linear-gradient(180deg,#f7d9a8,#e7a85c)"></div>
    <p>We need a Web design for a company doing business in Washington D.C. We deliver Hazard Line Training to Law Enforcement Agencies throughout the world. Our focus is</p>
    <div class="btn">Read More...</div>
  </article>
  <article class="card abs" style="left:526px">
    <h3>Solutions</h3>
    <div class="thumb" role="img" aria-label="Photo of documents and a pen in warm orange light" style="background:linear-gradient(135deg,#e3801e,#a53a0c)"></div>
    <p>We need a Web design for a company doing business in Washington D.C. We deliver Hazard Line Training to Law Enforcement Agencies throughout the world. Our focus is</p>
    <div class="btn">Read More...</div>
  </article>

  <h2 class="gallery-title abs">Gallery</h2>
  <figure class="tile abs" style="left:68px">
    <div class="img" role="img" aria-label="Photo of a car exploding in a test range" style="background:linear-gradient(180deg,#b9ab93,#d8c2a0 60%,#a59479)"></div>
    <figcaption class="cap">Hazard Line Training <svg width="11" height="11" viewBox="0 0 12 12"><path d="M6 0l6 6-6 6-6-6z" fill="#fff"/><path d="M3.5 6h5M6.5 4l2 2-2 2" stroke="#252525" fill="none" stroke-width="1.2"/></svg></figcaption>
  </figure>
  <figure class="tile abs" style="left:240px">
    <div class="img" role="img" aria-label="Photo of gloved hands holding a wired phone device" style="background:linear-gradient(135deg,#5b5a4a,#2e2d26 60%,#6b6553)"></div>
    <figcaption class="cap">Hazard Line Training <svg width="11" height="11" viewBox="0 0 12 12"><path d="M6 0l6 6-6 6-6-6z" fill="#fff"/><path d="M3.5 6h5M6.5 4l2 2-2 2" stroke="#252525" fill="none" stroke-width="1.2"/></svg></figcaption>
  </figure>
  <figure class="tile abs" style="left:409px">
    <div class="img" role="img" aria-label="Photo of soldiers gathered for a field briefing" style="background:linear-gradient(180deg,#9fb4c8,#8c8a78 45%,#7c7462)"></div>
    <figcaption class="cap">Hazard Line Training <svg width="11" height="11" viewBox="0 0 12 12"><path d="M6 0l6 6-6 6-6-6z" fill="#fff"/><path d="M3.5 6h5M6.5 4l2 2-2 2" stroke="#252525" fill="none" stroke-width="1.2"/></svg></figcaption>
  </figure>
  <figure class="tile abs" style="left:581px">
    <div class="img" role="img" aria-label="Photo of seized devices laid out on sand" style="background:linear-gradient(180deg,#a8a091,#8d8577)"></div>
    <figcaption class="cap">Hazard Line Training <svg width="11" height="11" viewBox="0 0 12 12"><path d="M6 0l6 6-6 6-6-6z" fill="#fff"/><path d="M3.5 6h5M6.5 4l2 2-2 2" stroke="#252525" fill="none" stroke-width="1.2"/></svg></figcaption>
  </figure>

  <section class="news abs">
    <h3>News &amp; Events</h3>
    <div class="bar"></div>
    <p>Successfully Delivering Tactical, Operational And Strategic Capabilites</p>
  </section>

  <footer class="footer abs">
    <div class="col about" style="left:86px">
      <h4>Hazard Line Training</h4>
      <h5>To Law Enforcement Agencies</h5>
      <p>We need a Web design for a company doing business in Washington D.C. We deliver Hazard Line Training to Law Enforcement Agencies throughout the world. Our focus is on Improvised Explosive Devices. We train Bomb Technicians and First</p>
    </div>
    <div class="col links" style="left:250px">
      <h4>Link</h4>
      <ul>
        <li>» Home</li><li>» About Us</li><li>» Capablities</li><li>» Mission</li><li>» News</li><li>» Gallery</li><li>» Contact Us</li>
      </ul>
    </div>
    <div class="col reach" style="left:416px">
      <h4>Reach Us</h4>
      <p>Hazard Line Training<br>To Law Enforcement Agencies<br>PO Box 40120<br>Easton, Texas 70010<br><br>Phone: (555) 010-2300<br>Fax: (555) 010-2301<br>Email: info@hazardlinetraining.com</p>
    </div>
    <div class="col letter" style="left:577px">
      <h4>News Letter</h4>
      <p>Enter your E-mail Address</p>
      <div class="field">E-mail Address</div>
      <div class="send">Send</div>
      <div class="mini"><span></span><span></span><span></span><span></span><span></span></div>
    </div>
  </footer>

</div>
</body>
</html>
```